Marlow Crest Holdings (Remodeling company) needs a logo and business card

We need a business card design for a new company. We "flip" upmarket houses (buy, remodel and sell) in the Austin, TX area. I'd like neutral colors (grey, white, gold black). I would like it to include a simple, clean logo. Our designs are modern and uncluttered and I would like that reflected in the business card design.

Target Market(s)

Young professionals, Families, Retirees. Our properties will sell for $750k+

Industry/Entity Type

Real Estate

Contact Information for Business Card

Marlow Crest Holdings
Nora Pellham
(555) 216 7042
Owner
Rory Tansil
(555) 638 1975
Realtor

Logo Text

Marlow Crest Holdings

Font styles to use
Serif
Script

Requirements
Must have
• Simple, classic design
Nice to have
• Clean lines, modern look
Should not have
• Too traditionally

```html
<!DOCTYPE html>
<html lang="en">
<head>
<meta charset="utf-8">
<title>Marlow Crest Holdings – Business Card</title>
<link href="https://fonts.googleapis.com/css2?family=Cinzel:wght@400&family=Quicksand:wght@400;500&display=swap" rel="stylesheet">
<style>
  :root {
    --backdrop: #d9d6d3;
    --card-black: #050505;
    --panel-grey: #232323;
    --gold: #c9962e;
    --gold-light: #f0cc6a;
    --gold-dark: #8a5f16;
    --text-light: #d6d6d6;
    --item-border: #3a3a3a;
  }
  * { box-sizing: border-box; margin: 0; padding: 0; }
  html, body { width: 1200px; height: 1000px; overflow: hidden; }
  body {
    background: var(--backdrop);
    display: flex;
    align-items: center;
    justify-content: center;
  }
  .business-card {
    position: relative;
    width: 332px;
    height: 580px;
    background: var(--card-black);
    box-shadow: 0 6px 18px rgba(0,0,0,0.35);
  }
  .gold-frame {
    position: absolute;
    inset: 22px 20px;
    border: 2px solid var(--gold);
    border-image: linear-gradient(135deg, var(--gold-dark), var(--gold-light), var(--gold-dark)) 1;
  }
  .brand {
    position: absolute;
    top: 50px;
    left: 40px;
    right: 40px;
    text-align: center;
  }
  .brand-dot {
    width: 20px;
    height: 20px;
    border-radius: 50%;
    background: var(--gold);
    margin: 0 auto 14px;
  }
  .brand-name {
    font-family: "Quicksand", sans-serif;
    font-weight: 500;
    font-size: 24px;
    line-height: 1.3;
    color: var(--gold);
  }
  .name-panel {
    position: absolute;
    top: 205px;
    left: 46px;
    width: 240px;
    height: 335px;
    background: var(--panel-grey);
    border: 1px solid var(--gold-dark);
  }
  .person-name {
    margin-top: 6px;
    text-align: center;
    font-family: "Cinzel", serif;
    font-size: 20px;
    color: var(--text-light);
  }
  .person-rule {
    width: 170px;
    height: 1px;
    margin: 2px auto 3px;
    background: var(--gold);
  }
  .person-title {
    text-align: center;
    font-family: "Cinzel", serif;
    font-size: 11px;
    color: var(--text-light);
  }
  .contact-list {
    position: absolute;
    top: 266px;
    left: 40px;
    width: 251px;
    list-style: none;
  }
  .contact-item {
    height: 48px;
    margin-bottom: 22px;
    background: var(--card-black);
    border: 1px solid var(--item-border);
    border-bottom-color: var(--gold-dark);
    display: flex;
    align-items: center;
    justify-content: center;
    font-family: "Quicksand", sans-serif;
    font-size: 13px;
    color: var(--text-light);
    box-shadow: 0 4px 6px rgba(0,0,0,0.6);
  }
</style>
</head>
<body>
  <article class="business-card">
    <div class="gold-frame"></div>
    <header class="brand">
      <div class="brand-dot"></div>
      <div class="brand-name">Marlow Crest Holdings</div>
    </header>
    <section class="name-panel">
      <div class="person-name">YOUR NAME</div>
      <div class="person-rule"></div>
      <div class="person-title">TITLE</div>
    </section>
    <ul class="contact-list">
      <li class="contact-item">A : Location</li>
      <li class="contact-item">P : 123-456-7890</li>
      <li class="contact-item">E : name@yourdomain.com</li>
      <li class="contact-item">W : yourdomain.com</li>
    </ul>
  </article>
</body>
</html>
```